Professional services firm needs whiteboard animation for internal campaign

We need animation to help demonstrate visually some changes that are occurring within our business model. This would be used for internal purposes only. I have put together a storyboard illustrating my vision which is attached below.
Our colors:

PRINT
PMS 1797 C
CMYK 00, 100, 99, 04

SCREEN
RGB 227, 27, 35
Hex #E31B23

```html
<!DOCTYPE html>
<html lang="en">
<head>
<meta charset="utf-8">
<title>Ridgeway — Animated Slides</title>
<link rel="stylesheet" href="https://fonts.googleapis.com/css2?family=Raleway:wght@300;400;700&family=Open+Sans:wght@400;600&display=swap">
<style>
  :root {
    --brand-red: #e31b23;
    --brand-red-deep: #c8151c;
    --sheet-grey: #acacac;
    --slide-white: #ffffff;
    --ink: #231f20;
    --label-ink: #1a1a1a;
    --icon-navy: #2c4a66;
    --icon-amber: #f5c542;
    --icon-teal: #27b3c3;
  }
  html, body {
    margin: 0;
    padding: 0;
    width: 1200px;
    height: 1200px;
    overflow: hidden;
    background: var(--sheet-grey);
  }
  .sheet {
    position: relative;
    width: 1200px;
    height: 1200px;
    font-family: "Raleway", sans-serif;
    color: var(--ink);
  }
  .brand {
    position: absolute;
    left: 68px;
    top: 62px;
    display: flex;
    align-items: center;
    gap: 10px;
    font-family: "Raleway", sans-serif;
    font-weight: 700;
    font-size: 30px;
    color: var(--brand-red);
  }
  .brand-dot {
    width: 22px;
    height: 22px;
    border-radius: 50%;
    background: var(--brand-red);
  }
  .features {
    position: absolute;
    left: 250px;
    top: 34px;
    margin: 0;
    padding: 0;
    list-style: none;
    font-weight: 300;
    font-size: 25px;
    line-height: 37.5px;
  }
  .page-number {
    position: absolute;
    right: 53px;
    top: 50px;
    font-weight: 300;
    font-size: 31px;
  }
  .slide {
    position: absolute;
    width: 515px;
    height: 448px;
    background: var(--slide-white);
    box-shadow: 6px 8px 14px rgba(0,0,0,0.35);
  }
  .slide-1 { left: 58px;  top: 176px; }
  .slide-2 { left: 633px; top: 176px; }
  .slide-3 { left: 58px;  top: 651px; }
  .slide-4 { left: 633px; top: 651px; }
  .slide-title {
    position: absolute;
    right: 19px;
    top: 18px;
    font-weight: 300;
    font-size: 24px;
  }
  .slide-art {
    position: absolute;
    inset: 0;
  }
  .intro-name {
    position: absolute;
    left: 0;
    right: 0;
    top: 196px;
    text-align: center;
    font-family: "Raleway", sans-serif;
    font-weight: 700;
    font-size: 44px;
    color: var(--brand-red);
  }
  .puzzle-label {
    font-family: "Open Sans", sans-serif;
    font-size: 11px;
    fill: #ffffff;
    text-anchor: middle;
  }
  .icon-label {
    font-family: "Open Sans", sans-serif;
    fill: var(--label-ink);
    text-anchor: middle;
  }
  .slide-3 .icon-label { font-size: 10.5px; }
  .slide-4 .icon-label { font-size: 8.6px; }
  .flow-arrow {
    stroke: var(--ink);
    stroke-width: 3;
    fill: none;
  }
</style>
</head>
<body>
<div class="sheet">

  <svg width="0" height="0" style="position:absolute" aria-hidden="true">
    <defs>
      <linearGradient id="puzzle-fill" x1="0" y1="0" x2="1" y2="1">
        <stop offset="0" stop-color="#e8343b"/>
        <stop offset="1" stop-color="#c8151c"/>
      </linearGradient>
      <linearGradient id="icon-fill" x1="0" y1="0" x2="1" y2="1">
        <stop offset="0" stop-color="#3c5a78"/>
        <stop offset="1" stop-color="#d8444a"/>
      </linearGradient>
      <marker id="arrowhead" viewBox="0 0 10 10" refX="7" refY="5" markerWidth="4" markerHeight="4" orient="auto-start-reverse">
        <path d="M0,0 L10,5 L0,10 z" fill="#231f20"/>
      </marker>
      <symbol id="service-puzzle" viewBox="119 94 279 249">
        <rect x="119" y="94" width="279" height="249" rx="26" fill="url(#puzzle-fill)"/>
        <text class="puzzle-label" x="285" y="129">MDM</text>
        <text class="puzzle-label" x="171" y="156">AMI</text>
        <text class="puzzle-label" x="361" y="188">SOM</text>
        <text class="puzzle-label" x="199" y="200">SGG</text>
        <text class="puzzle-label" x="161" y="269">Mgd.SVS</text>
        <text class="puzzle-label" x="322" y="269">ODM</text>
        <text class="puzzle-label" x="223" y="294">Training SVS</text>
        <text class="puzzle-label" x="255" y="339">Northmark</text>
      </symbol>
    </defs>
  </svg>

  <header>
    <div class="brand"><span class="brand-dot"></span>Ridgeway</div>
    <ul class="features">
      <li>Animated Slides</li>
      <li>100% Editable</li>
      <li>Animated Gifs</li>
    </ul>
    <div class="page-number">Page 01</div>
  </header>

  <section class="slide slide-1">
    <div class="slide-title">Slide 01</div>
    <div class="intro-name">Ridgeway</div>
  </section>

  <section class="slide slide-2">
    <div class="slide-title">Slide 02</div>
    <svg class="slide-art" viewBox="0 0 515 448" width="515" height="448">
      <svg x="119" y="94" width="279" height="249" role="img" aria-label="Red jigsaw illustration of the service pieces fitting together">
        <use href="#service-puzzle"/>
      </svg>
    </svg>
  </section>

  <section class="slide slide-3">
    <div class="slide-title">Slide 03</div>
    <svg class="slide-art" viewBox="0 0 515 448" width="515" height="448">
      <svg x="237" y="112" width="217" height="196" role="img" aria-label="Red jigsaw illustration of the service pieces fitting together">
        <use href="#service-puzzle"/>
      </svg>

      <line class="flow-arrow" x1="240" y1="175" x2="170" y2="137" marker-end="url(#arrowhead)"/>
      <line class="flow-arrow" x1="227" y1="228" x2="146" y2="228" marker-end="url(#arrowhead)"/>
      <line class="flow-arrow" x1="240" y1="286" x2="170" y2="326" marker-end="url(#arrowhead)"/>

      <rect x="96" y="86" width="68" height="51" rx="3" fill="url(#icon-fill)" role="img" aria-label="Meter dashboard with gears icon"/>
      <text class="icon-label" x="128" y="152">Meter Shop</text>

      <rect x="68" y="191" width="56" height="56" rx="3" fill="url(#icon-fill)" role="img" aria-label="Database stacks icon"/>
      <text class="icon-label" x="97" y="261">Infrastructure</text>

      <rect x="78" y="314" width="82" height="53" rx="3" fill="url(#icon-fill)" role="img" aria-label="Businessman beside billing document with gears"/>
      <text class="icon-label" x="114" y="382">Complex Billing</text>
    </svg>
  </section>

  <section class="slide slide-4">
    <div class="slide-title">Slide 04</div>
    <svg class="slide-art" viewBox="0 0 515 448" width="515" height="448">
      <svg x="167" y="124" width="178" height="159" role="img" aria-label="Red jigsaw illustration of the service pieces fitting together">
        <use href="#service-puzzle"/>
      </svg>

      <line class="flow-arrow" x1="167" y1="175" x2="110" y2="143" marker-end="url(#arrowhead)"/>
      <line class="flow-arrow" x1="157" y1="218" x2="90" y2="218" marker-end="url(#arrowhead)"/>
      <line class="flow-arrow" x1="167" y1="268" x2="110" y2="300" marker-end="url(#arrowhead)"/>
      <line class="flow-arrow" x1="347" y1="173" x2="404" y2="139" marker-end="url(#arrowhead)"/>
      <line class="flow-arrow" x1="356" y1="216" x2="423" y2="216" marker-end="url(#arrowhead)"/>
      <line class="flow-arrow" x1="347" y1="265" x2="404" y2="298" marker-end="url(#arrowhead)"/>

      <rect x="49" y="100" width="53" height="43" rx="3" fill="url(#icon-fill)" role="img" aria-label="Meter dashboard with gears icon"/>
      <text class="icon-label" x="75" y="155">Meter Shop</text>

      <rect x="25" y="187" width="47" height="46" rx="3" fill="url(#icon-fill)" role="img" aria-label="Database stacks icon"/>
      <text class="icon-label" x="50" y="246">Infrastructure</text>

      <rect x="35" y="289" width="68" height="44" rx="3" fill="url(#icon-fill)" role="img" aria-label="Businessman beside billing document with gears"/>
      <text class="icon-label" x="64" y="346">Complex Billing</text>

      <rect x="423" y="106" width="50" height="41" rx="3" fill="url(#icon-fill)" role="img" aria-label="Hand pressing a red gauge icon"/>
      <text class="icon-label" x="450" y="156">Meter Commands</text>

      <rect x="434" y="193" width="63" height="40" rx="3" fill="url(#icon-fill)" role="img" aria-label="Connected envelopes icon"/>
      <text class="icon-label" x="466" y="246">Outage Message</text>

      <rect x="420" y="296" width="65" height="37" rx="3" fill="url(#icon-fill)" role="img" aria-label="Businessman beside cloud transfer icon"/>
      <text class="icon-label" x="452" y="346">Usage Transactions</text>
    </svg>
  </section>

</div>
</body>
</html>
```